Webdesign für Bedrucken Papiertaschen, Schildern etc.
Zielgruppe
Wir bedrucken Papiertaschen, Papierbeutel, Laternen, Aluplaketten, Schilder, etc. und lasern Hundemarken. Zielgruppen von Privat bis Geschäftskunden
Aufgabenstellung
Der Shop sollte ein einfacher und kostengünstiger 'web2print'-shop werden. Wo die Kunden anhand von einem Editor Ihre Logos oder Druckvorlagen selber hochladen und/oder gestalten könne. Bisher haben die Kunden eifach ihre Bidldatei per E-Mail geschickt und wir haben diese dann weiter verarbeit.
Der Shop sollte, wenn möglich, günstig im Unterhalt sein, da wir nicht abschätzen können, wie gut diese laufen wird.
Wir haben wie 3 Bereich: 1. Papierbeutel/Taschen / 2. Stallplaketten (für z.B. Pferdesport) / 3. Diverses (Wie z.B. die Laternen, Schilder, Hundemarken, etc.)
Es würde sich um eine separate Webseite handeln. Daher ist bei Design freie Hand, eifach und klar... auch für nicht so ambitionierte Privatkunden oder kleine Unternehmen.

```html
<!DOCTYPE html>
<html lang="de">
<head>
<meta charset="utf-8">
<title>Tütenwerk – Papierbeutel &amp; Taschen</title>
<link href="https://fonts.googleapis.com/css2?family=Inter+Tight:wght@400;500;600;700&family=Inter:wght@400;500;600&family=JetBrains+Mono:wght@400;500;700&display=swap" rel="stylesheet">
<style>
:root{
  --ink:#161616;
  --muted:#6b6b6b;
  --line:#e4e4e2;
  --bg:#f4f4f3;
  --card:#ffffff;
  --red:#e0261c;
  --dark:#0f0f0f;
  --kraft:#c9a074;
}
*{box-sizing:border-box;margin:0;padding:0}
html,body{width:1200px;height:2329px;overflow:hidden}
body{background:var(--bg);font-family:"Inter",sans-serif;color:var(--ink);font-size:12px;position:relative}
.mono{font-family:"JetBrains Mono",monospace}
.wrap{position:absolute;left:47px;width:1105px}

/* topbar */
.topbar{height:24px;background:var(--dark);color:#fff;font-family:"JetBrains Mono",monospace;font-size:9px;letter-spacing:.04em;display:flex;justify-content:space-between;align-items:center;padding:0 47px}
.topbar .dot{display:inline-block;width:5px;height:5px;border-radius:50%;background:var(--red);margin-right:5px;vertical-align:middle}

/* header */
.header{height:67px;background:#fff;border-bottom:1px solid var(--line);display:flex;align-items:center;padding:0 47px;position:relative}
.brand{font-family:"Inter Tight",sans-serif;font-weight:700;font-size:15px;letter-spacing:-.02em}
.nav{position:absolute;left:251px;display:flex;gap:24px;font-size:12.5px}
.nav a{color:var(--ink);text-decoration:none;padding-bottom:4px}
.nav a.active{border-bottom:2px solid var(--red)}
.tools{margin-left:auto;display:flex;gap:14px;align-items:center}
.iconbtn{width:30px;height:30px;border:1px solid var(--line);border-radius:50%;display:flex;align-items:center;justify-content:center}
.cart{background:var(--red);color:#fff;border-radius:20px;height:31px;padding:0 12px;display:flex;align-items:center;gap:8px;font-weight:600;font-size:12px}
.cart .count{background:#fff;color:var(--red);width:16px;height:16px;border-radius:50%;font-size:9px;display:flex;align-items:center;justify-content:center}

.crumbs{top:113px;font-size:11.5px;color:var(--muted)}
.crumbs b{font-weight:400;color:var(--ink)}
.crumbs span{margin:0 9px}

/* hero */
.hero{top:147px;height:656px;background:var(--card);border:1px solid var(--line);border-radius:12px;overflow:hidden;display:flex}
.hero-left{width:525px;border-right:1px solid var(--line)}
.hero-photo{height:183px;background:linear-gradient(120deg,#263654 0%,#3d4d6c 30%,#c49a6c 55%,#d8b487 80%,#8b8a86 100%)}
.hero-text{padding:38px 27px}
.hero-text h1{font-family:"Inter Tight",sans-serif;font-weight:700;font-size:45px;line-height:1.05;letter-spacing:-.04em;margin-bottom:20px}
.hero-text p{font-size:12.5px;line-height:1.6;color:#333;width:410px}
.tags{display:flex;gap:7px;margin-top:18px}
.tag{font-family:"JetBrains Mono",monospace;font-size:9px;border:1px solid var(--line);border-radius:12px;padding:5px 9px}

.table{flex:1}
.thead{height:36px;display:flex;align-items:center;font-family:"JetBrains Mono",monospace;font-size:8.5px;color:var(--muted);letter-spacing:.06em;border-bottom:1px solid var(--line);padding-left:15px}
.row{height:77.5px;display:flex;align-items:center;padding:0 15px;border-bottom:1px solid var(--line)}
.row:last-child{border-bottom:0}
.thumb{width:54px;height:54px;border:1px solid var(--line);border-radius:6px;display:flex;align-items:center;justify-content:center;margin-right:12px}
.pname{width:248px;font-weight:600;font-size:12.5px}
.badge{display:inline-block;background:var(--red);color:#fff;font-family:"JetBrains Mono",monospace;font-size:7.5px;padding:3px 7px;border-radius:8px;margin-top:4px;font-weight:500}
.fmt{width:100px;font-family:"JetBrains Mono",monospace;font-size:10.5px;color:#333}
.price{width:80px;text-align:right;font-family:"JetBrains Mono",monospace;font-weight:700;font-size:11.5px}
.price small{display:block;font-weight:400;font-size:8.5px;color:var(--muted)}
.go{margin-left:auto;width:25px;height:25px;border:1px solid var(--line);border-radius:50%;display:flex;align-items:center;justify-content:center}

/* references */
.eyebrow{font-family:"JetBrains Mono",monospace;font-size:9px;letter-spacing:.08em;color:var(--muted)}
.ref-head{top:875px;display:flex;justify-content:space-between;align-items:flex-end;height:100px}
.ref-head h2{font-family:"Inter Tight",sans-serif;font-weight:700;font-size:36px;line-height:1.05;letter-spacing:-.035em;margin-top:8px}
.ref-head p{width:316px;font-size:12px;line-height:1.55;color:#333;margin-bottom:4px}
.grid{top:992px;display:grid;grid-template-columns:543px 543px;column-gap:19px;row-gap:20px}
.ref{height:265px;background:var(--card);border:1px solid var(--line);border-radius:12px;overflow:hidden;display:flex}
.ref .photo{width:278px}
.ref .info{padding:24px 22px;flex:1}
.ref h3{font-family:"Inter Tight",sans-serif;font-weight:600;font-size:19px;letter-spacing:-.02em;margin:6px 0 4px}
.ref .meta{font-family:"JetBrains Mono",monospace;font-size:9px;color:var(--muted);letter-spacing:.05em;margin-bottom:16px}
.kv{display:flex;margin-bottom:10px;font-size:10.5px;line-height:1.45}
.kv dt{width:77px;font-family:"JetBrains Mono",monospace;font-size:8.5px;color:var(--muted);letter-spacing:.05em;padding-top:1px}
.kv dd{flex:1}

.portfolio{top:1561px;height:82px;background:var(--card);border:1px solid var(--line);border-radius:12px;display:flex;align-items:center;padding:0 23px}
.portfolio h4{font-family:"Inter Tight",sans-serif;font-weight:500;font-size:19px;letter-spacing:-.01em;margin-top:6px}
.btns{margin-left:auto;display:flex;gap:9px}
.btn{height:41px;border-radius:21px;display:flex;align-items:center;gap:8px;padding:0 19px;font-weight:600;font-size:12px}
.btn.red{background:var(--red);color:#fff}
.btn.ghost{border:1px solid var(--ink)}

/* advice */
.advice{top:1710px;height:256px;background:var(--card);border:1px solid var(--line);border-radius:12px;padding:38px 40px;display:flex}
.advice-text{width:570px}
.advice h2{font-family:"Inter Tight",sans-serif;font-weight:700;font-size:30px;letter-spacing:-.03em;margin:8px 0 12px}
.advice p{font-size:12px;line-height:1.6;color:#333;width:390px;margin-bottom:17px}
.facts{display:grid;grid-template-columns:220px 220px;gap:10px;margin-top:11px}
.fact{border:1px solid var(--line);border-radius:8px;height:74px;padding:18px 15px}
.fact b{display:block;font-family:"Inter Tight",sans-serif;font-size:19px;font-weight:600;margin-top:6px}

/* footer */
.footer{position:absolute;top:2027px;left:0;width:1200px;height:302px;background:var(--dark);color:#fff}
.fbrand{position:absolute;left:47px;top:40px;font-family:"Inter Tight",sans-serif;font-weight:700;font-size:14px;display:flex;align-items:center;gap:6px}
.fbrand i{width:9px;height:9px;background:#fff;display:block}
.fabout{position:absolute;left:47px;top:90px;width:260px;font-size:11px;line-height:1.6;color:#ddd}
.fcol{position:absolute;top:44px;font-size:11px;line-height:21.5px;color:#ddd}
.fcol h5{font-size:11.5px;font-weight:600;letter-spacing:.05em;color:#fff;margin-bottom:12px}
.fbottom{position:absolute;left:47px;right:47px;top:248px;border-top:1px solid #2a2a2a;padding-top:22px;display:flex;justify-content:space-between;font-family:"JetBrains Mono",monospace;font-size:9.5px;color:#ccc}
.pay{display:flex;gap:15px}
</style>
</head>
<body>

<div class="topbar">
  <div><span class="dot"></span>VERSAND CH AB CHF 9.50 — DE/FR/IT VERFÜGBAR</div>
  <div>DRUCK IN 3–5 WERKTAGEN · LASERGRAVUR AB 24 H</div>
  <div>HILFE? +41 44 555 18 40</div>
</div>

<header class="header">
  <div class="brand">Tütenwerk</div>
  <nav class="nav">
    <a class="active">Papierbeutel &amp; Taschen</a><a>Stallplaketten</a><a>Hundemarken &amp; Diverses</a><a>Über uns</a><a>Hilfe</a>
  </nav>
  <div class="tools">
    <div class="iconbtn"><svg width="12" height="12" viewBox="0 0 12 12" fill="none" stroke="#161616" stroke-width="1.3"><circle cx="5" cy="5" r="3.8"/><path d="M8 8l3 3"/></svg></div>
    <div class="iconbtn"><svg width="12" height="12" viewBox="0 0 12 12" fill="none" stroke="#161616" stroke-width="1.2"><circle cx="6" cy="4" r="2.4"/><path d="M1.5 11c.6-2.6 2.4-3.8 4.5-3.8s3.9 1.2 4.5 3.8"/></svg></div>
    <div class="cart"><svg width="12" height="12" viewBox="0 0 12 12" fill="none" stroke="#fff" stroke-width="1.2"><path d="M1 1.5h2l1.2 6h5.6l1-4.2H3.4"/><circle cx="5" cy="10" r=".8"/><circle cx="9" cy="10" r=".8"/></svg>Warenkorb<span class="count">0</span></div>
  </div>
</header>

<div class="wrap crumbs">Start<span>›</span>Sortiment<span>›</span><b>Papierbeutel &amp; Taschen</b></div>

<section class="wrap hero">
  <div class="hero-left">
    <div class="hero-photo" role="img" aria-label="Foto: bedruckte braune Papiertragetasche vor dunkelblauen Einkaufstaschen"></div>
    <div class="hero-text">
      <h1>Papierbeutel &amp;<br>Taschen</h1>
      <p>Für Bäckereien, Boutiquen, Take-Away, Messeauftritte und Eventbedarf. Bedruckt im Flexo- oder Digitaldruck — vom 1-Farb-Logo bis zur Vollfläche. ForstZert-zertifiziertes Papier, schweizweite Lieferung in 3–5 Tagen.</p>
      <div class="tags"><span class="tag">FLEXODRUCK</span><span class="tag">DIGITALDRUCK</span><span class="tag">FORSTZERT</span><span class="tag">LEBENSMITTELECHT</span></div>
    </div>
  </div>
  <div class="table">
    <div class="thead"><span style="width:314px">PRODUKT</span><span style="width:159px">FORMAT</span><span>AB</span></div>

    <div class="row"><div class="thumb"><svg width="28" height="38"><rect x="1" y="1" width="26" height="36" fill="#c9a074"/><rect x="8" y="15" width="12" height="7" fill="#e0261c"/></svg></div><div class="pname">Faltenbeutel braun<br><span class="badge">BESTSELLER</span></div><div class="fmt">7 Grössen</div><div class="price">CHF 0.18<small>pro Stk.</small></div><div class="go"><svg width="9" height="9" viewBox="0 0 9 9" fill="none" stroke="#161616" stroke-width="1.1"><path d="M1 4.5h7M5.5 2l2.5 2.5L5.5 7"/></svg></div></div>

    <div class="row"><div class="thumb"><svg width="28" height="38"><path d="M1 37V12C1 5 6 1 14 1s13 4 13 11v25z" fill="#efe1c3"/><rect x="9" y="20" width="10" height="6" fill="#e7766c"/></svg></div><div class="pname">Bäcker-/Brötchenbeutel</div><div class="fmt">5 Grössen</div><div class="price">CHF 0.14<small>pro Stk.</small></div><div class="go"><svg width="9" height="9" viewBox="0 0 9 9" fill="none" stroke="#161616" stroke-width="1.1"><path d="M1 4.5h7M5.5 2l2.5 2.5L5.5 7"/></svg></div></div>

    <div class="row"><div class="thumb"><svg width="34" height="40"><path d="M9 10C9 3 14 3 14 10M20 10C20 3 25 3 25 10" fill="none" stroke="#3a2a1c" stroke-width="1.3"/><rect x="2" y="9" width="30" height="30" fill="#c9a074"/><rect x="8" y="20" width="18" height="7" fill="#e0261c"/></svg></div><div class="pname">Tragetaschen mit Henkel</div><div class="fmt">4 Grössen</div><div class="price">CHF 0.62<small>pro Stk.</small></div><div class="go"><svg width="9" height="9" viewBox="0 0 9 9" fill="none" stroke="#161616" stroke-width="1.1"><path d="M1 4.5h7M5.5 2l2.5 2.5L5.5 7"/></svg></div></div>

    <div class="row"><div class="thumb"><svg width="26" height="38"><rect x="1" y="1" width="24" height="36" fill="#fff" stroke="#e4e4e2"/><rect x="8" y="17" width="10" height="3" fill="#e0261c"/></svg></div><div class="pname">Flachbeutel weiss</div><div class="fmt">6 Grössen</div><div class="price">CHF 0.16<small>pro Stk.</small></div><div class="go"><svg width="9" height="9" viewBox="0 0 9 9" fill="none" stroke="#161616" stroke-width="1.1"><path d="M1 4.5h7M5.5 2l2.5 2.5L5.5 7"/></svg></div></div>

    <div class="row"><div class="thumb"><svg width="34" height="34"><path d="M1 3h32L17 33z" fill="#c9a074"/><rect x="11" y="6" width="12" height="4" fill="#e0261c"/></svg></div><div class="pname">Spitzbeutel</div><div class="fmt">3 Grössen</div><div class="price">CHF 0.22<small>pro Stk.</small></div><div class="go"><svg width="9" height="9" viewBox="0 0 9 9" fill="none" stroke="#161616" stroke-width="1.1"><path d="M1 4.5h7M5.5 2l2.5 2.5L5.5 7"/></svg></div></div>

    <div class="row"><div class="thumb"><svg width="34" height="42"><path d="M9 10C9 3 14 3 14 10M20 10C20 3 25 3 25 10" fill="none" stroke="#e0261c" stroke-width="1.3"/><rect x="2" y="9" width="30" height="32" fill="#fff" stroke="#e4e4e2"/><rect x="8" y="22" width="18" height="7" fill="#e0261c"/></svg></div><div class="pname">Geschenktaschen</div><div class="fmt">5 Grössen</div><div class="price">CHF 1.20<small>pro Stk.</small></div><div class="go"><svg width="9" height="9" viewBox="0 0 9 9" fill="none" stroke="#161616" stroke-width="1.1"><path d="M1 4.5h7M5.5 2l2.5 2.5L5.5 7"/></svg></div></div>

    <div class="row"><div class="thumb"><svg width="28" height="38"><rect x="1" y="1" width="26" height="36" fill="#c9a074"/><path d="M1 7h26" stroke="#a47b51"/><rect x="8" y="16" width="12" height="7" fill="#e0261c"/></svg></div><div class="pname">Bodenbeutel mit Klappe</div><div class="fmt">4 Grössen</div><div class="price">CHF 0.34<small>pro Stk.</small></div><div class="go"><svg width="9" height="9" viewBox="0 0 9 9" fill="none" stroke="#161616" stroke-width="1.1"><path d="M1 4.5h7M5.5 2l2.5 2.5L5.5 7"/></svg></div></div>

    <div class="row"><div class="thumb"><svg width="28" height="38"><path d="M1 37V12C1 5 6 1 14 1s13 4 13 11v25z" fill="#efe1c3"/><rect x="9" y="20" width="10" height="6" fill="#e7766c"/></svg></div><div class="pname">Kreuzbodenbeutel</div><div class="fmt">5 Grössen</div><div class="price">CHF 0.28<small>pro Stk.</small></div><div class="go"><svg width="9" height="9" viewBox="0 0 9 9" fill="none" stroke="#161616" stroke-width="1.1"><path d="M1 4.5h7M5.5 2l2.5 2.5L5.5 7"/></svg></div></div>
  </div>
</section>

<section class="wrap ref-head">
  <div>
    <div class="eyebrow">REFERENZEN</div>
    <h2>Aus über 60 Jahren<br>Druckerei.</h2>
  </div>
  <p>Ein paar Kundenarbeiten als Inspiration. Anonymisiert auf Wunsch — sagen Sie uns einfach Bescheid, wenn Sie Ihre eigene Auflage nicht im Schaufenster sehen möchten.</p>
</section>

<section class="wrap grid">
  <article class="ref">
    <div class="photo" role="img" aria-label="Foto: bedruckte Mehlsäcke aus Papier im Bäckereiregal" style="background:linear-gradient(135deg,#dfe3e6,#c9b9a0 55%,#8d6d4f)"></div>
    <div class="info">
      <div class="eyebrow">BÄCKEREI</div><h3>Kunde #1</h3><div class="meta">BÄCKEREI · SEIT 1962</div>
      <dl><div class="kv"><dt>PRODUKT</dt><dd>Faltenbeutel braun, M · 16×26 cm</dd></div><div class="kv"><dt>AUFLAGE</dt><dd>2'400 Stk. · 1-farbig Farbfächer 7621</dd></div></dl>
    </div>
  </article>
  <article class="ref">
    <div class="photo" role="img" aria-label="Foto: Tragetasche an einer Backsteinwand hängend" style="background:linear-gradient(135deg,#3a2b24,#a8866c 40%,#d8c8b4 60%,#7a3b2c)"></div>
    <div class="info">
      <div class="eyebrow">BOUTIQUE</div><h3>Kunde #2</h3><div class="meta">ATELIER · ZÜRICH</div>
      <dl><div class="kv"><dt>PRODUKT</dt><dd>Tragetasche mit Kordelhenkel · 32×40 cm</dd></div><div class="kv"><dt>AUFLAGE</dt><dd>800 Stk. · 1-farbig Schwarz · Hochglanz</dd></div></dl>
    </div>
  </article>
  <article class="ref">
    <div class="photo" role="img" aria-label="Foto: bedruckter Pizzakarton auf dunklem Holztisch" style="background:radial-gradient(circle at 50% 50%,#e6ddd0 0,#cfc3b2 38%,#4a2e22 60%,#2a1a12)"></div>
    <div class="info">
      <div class="eyebrow">TAKE-AWAY</div><h3>Kunde #3</h3><div class="meta">PIZZA · BERN</div>
      <dl><div class="kv"><dt>PRODUKT</dt><dd>Karton braun · 18 cm</dd></div><div class="kv"><dt>AUFLAGE</dt><dd>5'200 Stk. · 2-farbig Rot/Schwarz</dd></div></dl>
    </div>
  </article>
  <article class="ref">
    <div class="photo" role="img" aria-label="Foto: weisse Stofftasche hängt zwischen grünen Pflanzen" style="background:radial-gradient(circle at 60% 55%,#efe9dc 0,#e4dccb 25%,#5e6b3a 55%,#2c3418)"></div>
    <div class="info">
      <div class="eyebrow">EVENT</div><h3>Kunde #4</h3><div class="meta">GURTEN · 2026</div>
      <dl><div class="kv"><dt>PRODUKT</dt><dd>Geschenktasche Premium · 24×31 cm</dd></div><div class="kv"><dt>AUFLAGE</dt><dd>1'600 Stk. · 4-farbig CMYK</dd></div></dl>
    </div>
  </article>
</section>

<section class="wrap portfolio">
  <div><div class="eyebrow">MEHR BEISPIELE?</div><h4>Unser PDF-Portfolio · 48 Seiten Druckarbeiten</h4></div>
  <div class="btns">
    <div class="btn red">Portfolio (PDF) <svg width="10" height="9" viewBox="0 0 10 9" fill="none" stroke="#fff" stroke-width="1.2"><path d="M1 4.5h8M6 1.5l3 3-3 3"/></svg></div>
    <div class="btn ghost">Materialmuster gratis</div>
  </div>
</section>

<section class="wrap advice">
  <div class="advice-text">
    <div class="eyebrow">BERATUNG</div>
    <h2>Ihre Auflage ist speziell?</h2>
    <p>Mengen über 25'000, ungewöhnliche Formate, Sondermaterialien oder Veredelungen wie Heissprägung, Hochglanz oder Stanzungen — wir offerieren in 24 Std. Telefonisch oder per Formular.</p>
    <div class="btns" style="margin-left:0"><div class="btn red">Offerte anfordern</div><div class="btn ghost">+41 44 555 18 40</div></div>
  </div>
  <div class="facts">
    <div class="fact"><div class="eyebrow">ANTWORTZEIT</div><b>&lt; 24 h</b></div>
    <div class="fact"><div class="eyebrow">MINDESTAUFLAGE</div><b>100 Stk.</b></div>
    <div class="fact"><div class="eyebrow">LIEFERUNG</div><b>3–5 Tage</b></div>
    <div class="fact"><div class="eyebrow">EXPRESS</div><b>ab 48 h</b></div>
  </div>
</section>

<footer class="footer">
  <div class="fbrand"><i></i>Tütenwerk</div>
  <p class="fabout">Druckerei und Lasergravur aus der Schweiz. Wir bedrucken Papierbeutel, Stallplaketten, Laternen, Schilder und lasern Hundemarken — vom Einzelstück bis zur Grossauflage.</p>
  <div class="fcol" style="left:481px"><h5>PRODUKTE</h5>Papierbeutel<br>Papiertaschen<br>Stallplaketten<br>Hundemarken<br>Laternen &amp; Schilder<br>Aluplaketten</div>
  <div class="fcol" style="left:718px"><h5>SERVICE</h5>Druckvorlagen-Editor<br>Druckdaten anliefern<br>Materialmuster bestellen<br>Mengenrabatte<br>Versand &amp; Lieferung<br>Hilfe &amp; FAQ</div>
  <div class="fcol" style="left:956px"><h5>FIRMA</h5>Über uns<br>Nachhaltigkeit<br>Geschäftskunden<br>Kontakt<br>AGB<br>Impressum</div>
  <div class="fbottom">
    <span>© 2026 Tütenwerk · Brennhalde Druck AG · CH-8999 Mattenbach / Zürich</span>
    <span class="pay"><span>PayFlink</span><span>Kartenblau</span><span>Ringkarte</span><span>Rechnung</span><span>Postkasse</span></span>
  </div>
</footer>

</body>
</html>
```